Name card design for Southeast Asian Crowdfunding Startup

We need a double paged design for our company name cards.

We are a Singapore based crowd funding startup looking to operate regionally in Southeast Asia. Our service will be to match-make borrowers and lenders for loans, equity, property etc.

We have a logo already designed and hope for that to be used in the name card.

Industry/Entity Type

It Company

```html
<!DOCTYPE html>
<html lang="en">
<head>
<meta charset="utf-8">
<title>Kota Lending Circle – Name Card</title>
<link href="https://fonts.googleapis.com/css2?family=Tenor+Sans&family=Roboto+Condensed:wght@300;700&display=swap" rel="stylesheet">
<style>
  :root {
    --backdrop: #3a3a3a;
    --card-cream: #fbf1e2;
    --mosaic-teal: #7fc8cc;
    --mosaic-blue: #2f6aa8;
    --mosaic-amber: #e5b35a;
    --ink: #1c1c1c;
    --orange: #f7931e;
    --brown: #6f4824;
    --white: #ffffff;
    --paper: #fdfdfd;
    --accent-circle: #e4287c;
  }
  * { margin: 0; padding: 0; box-sizing: border-box; }
  html, body { width: 1200px; height: 1000px; overflow: hidden; }
  body { background: var(--backdrop); position: relative; }

  .card {
    position: absolute;
    width: 807px;
    height: 440px;
    overflow: hidden;
  }

  /* Front side */
  .card--front {
    left: 90px; top: 47px;
    background: var(--card-cream);
  }
  .front__backdrop {
    position: absolute; inset: 0;
    background:
      linear-gradient(180deg, rgba(251,241,226,0) 45%, rgba(251,241,226,0.85) 90%),
      linear-gradient(90deg, var(--card-cream) 0%, #f6e6cf 22%, var(--mosaic-teal) 50%, var(--mosaic-blue) 78%, var(--mosaic-amber) 100%);
  }
  .front__mark {
    position: absolute;
    left: 150px; top: 170px;
    width: 90px; height: 90px;
    border-radius: 50%;
    background: var(--accent-circle);
  }
  .front__wordmark {
    position: absolute;
    left: 407px; top: 112px;
    font-family: "Tenor Sans", sans-serif;
    font-size: 78px;
    line-height: 72px;
    color: var(--ink);
    letter-spacing: 1px;
  }

  /* Back side */
  .card--back {
    left: 299px; top: 510px;
    display: flex;
  }
  .back__contact {
    width: 502px; height: 100%;
    background: var(--orange);
    display: flex; flex-direction: column; align-items: center;
    padding-top: 22px;
    font-family: "Roboto Condensed", sans-serif;
    color: var(--brown);
  }
  .contact__name {
    font-size: 60px; line-height: 70px;
    color: var(--white);
    margin-bottom: 8px;
  }
  .contact__name .first { font-weight: 700; }
  .contact__name .last { font-weight: 300; }
  .contact__icon {
    width: 48px; height: 48px;
    margin: 6px 0 4px;
  }
  .contact__line {
    font-weight: 700;
    font-size: 44px; line-height: 50px;
  }
  .back__brand {
    flex: 1;
    background: var(--paper);
    display: flex; align-items: center; justify-content: center;
    gap: 14px;
  }
  .brand__circle {
    width: 36px; height: 36px; border-radius: 50%;
    background: var(--accent-circle);
  }
  .brand__name {
    font-family: "Tenor Sans", sans-serif;
    font-size: 24px; line-height: 22px;
    color: var(--ink);
  }
</style>
</head>
<body>

  <section class="card card--front">
    <div class="front__backdrop" role="img" aria-label="Soft mosaic of cream, teal, blue and amber squares"></div>
    <div class="front__mark"></div>
    <h1 class="front__wordmark">KOTA<br>LENDING<br>CIRCLE</h1>
  </section>

  <section class="card card--back">
    <div class="back__contact">
      <p class="contact__name"><span class="first">Daniel</span><span class="last">Reyes</span></p>

      <svg class="contact__icon" viewBox="0 0 48 48" aria-hidden="true">
        <circle cx="24" cy="24" r="24" fill="var(--brown)"/>
        <path d="M17 13c1-1 2.5-1 3.2 0l2.6 3.8c.6.9.4 2-.3 2.7l-1.7 1.6c1.2 2.6 3.3 4.8 5.9 6l1.6-1.7c.7-.7 1.8-.9 2.7-.3l3.8 2.6c1 .7 1 2.2 0 3.2l-1.8 1.8c-1.4 1.4-3.6 1.7-5.4.8-5.4-2.8-9.8-7.2-12.6-12.6-.9-1.8-.6-4 .8-5.4z" fill="var(--orange)"/>
      </svg>
      <p class="contact__line">0800.555.0192</p>

      <svg class="contact__icon" viewBox="0 0 48 48" aria-hidden="true">
        <circle cx="24" cy="24" r="24" fill="var(--brown)"/>
        <rect x="12" y="16" width="24" height="16" fill="none" stroke="var(--orange)" stroke-width="2.4"/>
        <path d="M12 16l12 9 12-9M12 32l9-8M36 32l-9-8" fill="none" stroke="var(--orange)" stroke-width="2.2"/>
      </svg>
      <p class="contact__line">daniel@kotalc.com</p>

      <svg class="contact__icon" viewBox="0 0 48 48" aria-hidden="true">
        <circle cx="24" cy="24" r="24" fill="var(--brown)"/>
        <g fill="none" stroke="var(--orange)" stroke-width="2">
          <circle cx="24" cy="24" r="13"/>
          <ellipse cx="24" cy="24" rx="6" ry="13"/>
          <path d="M11 24h26M13 17h22M13 31h22M24 11v26"/>
        </g>
      </svg>
      <p class="contact__line">www.kotalc.com</p>
    </div>

    <div class="back__brand">
      <div class="brand__circle"></div>
      <p class="brand__name">KOTA<br>LENDING<br>CIRCLE</p>
    </div>
  </section>

</body>
</html>
```